Love pets? Create a veterinary business card that aligns with our new revamped website.

Greetings! We are a five-doctor veterinary hospital that seeks your expertise in designing a new business card that harmonizes with our recently revitalized website: www.tqrn.net. The card should feature our logo, the five doctors, operating hours, contact information, and communicate our purpose and personality.

Contact Information for Business Card

TBA

```html
<!DOCTYPE html>
<html lang="en">
<head>
<meta charset="utf-8">
<title>Maple Hollow Veterinary Hospital – Business Card</title>
<link href="https://fonts.googleapis.com/css2?family=Dancing+Script:wght@600&family=Poppins:wght@400;500;600&display=swap" rel="stylesheet">
<style>
  :root{
    --bg:#3a3a3a;
    --green:#4a8a3f;
    --brown:#8a6320;
    --gold:#d9a441;
    --white:#ffffff;
    --ink:#555555;
  }
  *{box-sizing:border-box;margin:0;padding:0}
  html,body{width:1200px;height:689px;overflow:hidden;background:var(--bg);font-family:"Poppins",sans-serif}
  .stage{position:relative;width:1200px;height:689px}
  .card{position:absolute;top:190px;width:540px;height:309px;border-radius:18px;overflow:hidden}
  .card--back{left:40px;background:var(--green);color:var(--white)}
  .card--front{left:620px;background:var(--white)}

  /* brand lockup */
  .brand{display:flex;align-items:center;gap:10px}
  .brand__mark{width:16px;height:16px;border-radius:50%;flex:none}
  .brand__name{font-weight:500;line-height:1.15}
  .brand__sub{display:block;font-size:11px;letter-spacing:.5px}
  .card--back .brand{position:absolute;top:30px;left:0;right:0;justify-content:center}
  .card--back .brand__mark{background:var(--white)}
  .card--back .brand__name{color:var(--white);font-size:22px}

  /* hours frame */
  .hours{position:absolute;left:34px;right:34px;top:112px;bottom:30px;border:1.5px solid var(--white)}
  .hours__title,.hours__closed{position:absolute;left:50%;transform:translateX(-50%);background:var(--green);padding:0 12px;white-space:nowrap;font-weight:500;font-size:14px;letter-spacing:.6px}
  .hours__title{top:-11px}
  .hours__closed{bottom:-11px;font-weight:400;font-size:13px;letter-spacing:.3px}
  .hours__cols{position:absolute;top:40px;left:30px;right:30px;display:flex;justify-content:space-between}
  .hours__list{list-style:none;font-size:14px;line-height:1.9}
  .hours__list li{display:flex;gap:16px}
  .hours__day{width:36px}

  /* front */
  .card--front .brand{position:absolute;top:34px;left:34px}
  .card--front .brand__mark{background:var(--green);width:20px;height:20px}
  .card--front .brand__name{color:var(--green);font-size:25px}
  .card--front .brand__sub{font-size:12px}
  .doctors{position:absolute;left:34px;top:116px;list-style:none;font-family:"Dancing Script",cursive;font-weight:600;font-size:24px;line-height:1.12}
  .doctors li:nth-child(odd){color:var(--green)}
  .doctors li:nth-child(even){color:var(--brown)}
  .divider{position:absolute;left:292px;top:122px;width:1px;height:140px;background:var(--gold)}
  .contact{position:absolute;left:310px;top:132px;list-style:none;font-size:12.5px;color:var(--ink);line-height:1.4}
  .contact li{display:flex;gap:10px;align-items:flex-start;margin-bottom:6px}
  .contact svg{width:13px;height:13px;flex:none;margin-top:3px;fill:var(--green)}
  .rule{position:absolute;left:0;right:0;bottom:30px;height:3px;background:var(--brown)}
  .band{position:absolute;left:0;right:0;bottom:0;height:26px;background:var(--green)}
</style>
</head>
<body>
<main class="stage">

  <section class="card card--back" aria-label="Card back: hospital hours">
    <div class="brand">
      <span class="brand__mark"></span>
      <p class="brand__name">Maple Hollow<span class="brand__sub">VETERINARY HOSPITAL</span></p>
    </div>
    <div class="hours">
      <h2 class="hours__title">HOSPITAL HOURS</h2>
      <div class="hours__cols">
        <ul class="hours__list">
          <li><span class="hours__day">Mon</span><span>7:00am – 6:00pm</span></li>
          <li><span class="hours__day">Tue</span><span>7:00am – 6:00pm</span></li>
          <li><span class="hours__day">Wed</span><span>7:00am – 6:00pm</span></li>
        </ul>
        <ul class="hours__list">
          <li><span class="hours__day">Thu</span><span>7:00am – 6:00pm</span></li>
          <li><span class="hours__day">Fri</span><span>7:00am – 6:00pm</span></li>
          <li><span class="hours__day">Sat</span><span>8:00am – 12:00pm</span></li>
        </ul>
      </div>
      <p class="hours__closed">Sunday: Closed</p>
    </div>
  </section>

  <section class="card card--front" aria-label="Card front: doctors and contact">
    <div class="brand">
      <span class="brand__mark"></span>
      <p class="brand__name">Maple Hollow<span class="brand__sub">VETERINARY HOSPITAL</span></p>
    </div>
    <ul class="doctors">
      <li>Owen Pratt, DVM</li>
      <li>Nora Keel, DVM</li>
      <li>Julia Reyes, DVM</li>
      <li>Hannah Lowe, DVM</li>
      <li>Lena Ford, DVM</li>
    </ul>
    <div class="divider"></div>
    <ul class="contact">
      <li><svg viewBox="0 0 24 24" aria-hidden="true"><path d="M6.6 10.8a15 15 0 0 0 6.6 6.6l2.2-2.2a1 1 0 0 1 1-.25 11.4 11.4 0 0 0 3.6.57 1 1 0 0 1 1 1V20a1 1 0 0 1-1 1A17 17 0 0 1 3 4a1 1 0 0 1 1-1h3.5a1 1 0 0 1 1 1c0 1.25.2 2.45.57 3.6a1 1 0 0 1-.25 1z"/></svg><span>(555) 204-1187<br>(555) 204-1190</span></li>
      <li><svg viewBox="0 0 24 24" aria-hidden="true"><path d="M2 5h20v14H2zm2 2v.5l8 5 8-5V7zm0 3v7h16v-7l-8 5z"/></svg><span>info@tqrn.net</span></li>
      <li><svg viewBox="0 0 24 24" aria-hidden="true"><path d="M12 2a7 7 0 0 0-7 7c0 5 7 13 7 13s7-8 7-13a7 7 0 0 0-7-7zm0 9.5A2.5 2.5 0 1 1 12 6.5a2.5 2.5 0 0 1 0 5z"/></svg><span>4820 Cedar Bend Road<br>Brookfield, TX 75012</span></li>
    </ul>
    <div class="rule"></div>
    <div class="band"></div>
  </section>

</main>
</body>
</html>
```